Business Card Design

Brambledown Pantry is the name of my health coaching business. My tag line is "Where good health meets real life." I will be working with clients one-on-one and in groups. My target clients are women "of a certain age" who want to be more comfortable in their own skin. We will work together in a 6-month program. The coaching sessions will take place in my kitchen. I will also be conducting monthly cooking classes and field trips - to farmer's markets, speciality markets etc.. for my clients.
Updates

the business name is Brambledown Pantry - I'm not sure how the p got in there at the end of the name

Thank you

Please include the website - www.brambledownpantry-example.com and the tag line:

Where good health meets real life on the business card.

Thank you

Please add the phone number to the business card - sorry, I forgot to state that in the original brief

(555) 274-8150

Target Market(s)

Women "of a certain age" who want to be more comfortable in their own skin

Industry/Entity Type

Cooking

Contact Information for Business Card

Brambledown Pantry
Where good health meets real life

Rosalind Hartwell
Health Coach
(555) 274-8150

Font styles to use
Serif
Sans Serif

Requirements
Must have
• front & back design
I typical like soft colors - and have tended toward greens over time - I'm open although I would not like bright reds, yellows etc..

```html
<!DOCTYPE html>
<html lang="en">
<head>
<meta charset="utf-8">
<title>Brambledown Pantry – Business Card</title>
<link rel="stylesheet" href="https://fonts.googleapis.com/css2?family=Open+Sans:ital,wght@0,400;0,600;0,700;1,400;1,600&display=swap">
<style>
  :root {
    --page-bg: #e4e6e2;
    --card-green: #3f8b3b;
    --card-green-light: #4f9a49;
    --card-green-soft: #5aa553;
    --ink-pale: #cdeebe;
    --ink-dark: #2d6a2a;
    --badge: #c8efb5;
    --shadow: rgba(0, 0, 0, 0.28);
  }
  * { box-sizing: border-box; margin: 0; padding: 0; }
  html, body {
    width: 1200px;
    height: 900px;
    overflow: hidden;
    background: var(--page-bg);
    font-family: "Open Sans", Arial, sans-serif;
  }
  .sheet {
    position: relative;
    width: 1200px;
    height: 900px;
  }
  .card {
    position: absolute;
    left: 250px;
    width: 700px;
    height: 400px;
    background: var(--card-green);
    box-shadow: 0 10px 24px var(--shadow);
    overflow: hidden;
    color: var(--ink-pale);
  }
  .card--back { top: 40px; }
  .card--front { top: 470px; }

  .utensil-pattern {
    position: absolute;
    inset: 0;
    background:
      radial-gradient(ellipse at 30% 35%, var(--card-green-soft) 0%, transparent 55%),
      radial-gradient(ellipse at 75% 60%, var(--card-green-light) 0%, transparent 60%),
      linear-gradient(135deg, var(--card-green-light), var(--card-green));
    opacity: 0.8;
  }

  /* Back */
  .back-message {
    position: absolute;
    left: 70px;
    top: 70px;
    width: 560px;
    font-size: 25px;
    font-style: italic;
    line-height: 1.3;
    letter-spacing: 0.5px;
    text-align: center;
  }
  .social {
    position: absolute;
    left: 200px;
    top: 260px;
    width: 300px;
    text-align: center;
  }
  .social-mark {
    display: block;
    width: 26px;
    height: 26px;
    margin: 0 auto 4px;
    background: var(--ink-pale);
    border-radius: 3px;
  }
  .social-handle {
    display: block;
    font-size: 22px;
    font-weight: 600;
    padding-bottom: 4px;
    border-bottom: 3px solid var(--ink-pale);
  }

  /* Front */
  .coach {
    position: absolute;
    right: 36px;
    top: 38px;
    text-align: right;
  }
  .coach-name {
    display: inline-block;
    background: var(--badge);
    color: var(--ink-dark);
    font-size: 26px;
    font-weight: 600;
    padding: 2px 12px;
    border-radius: 3px;
  }
  .coach-title {
    display: block;
    font-size: 26px;
    font-weight: 600;
    margin-top: 2px;
    padding-right: 12px;
  }
  .brand {
    position: absolute;
    left: 40px;
    top: 120px;
    white-space: nowrap;
  }
  .brand-name {
    font-size: 64px;
    font-weight: 700;
    letter-spacing: -1px;
    line-height: 1;
  }
  .brand-name .brand-sub {
    font-size: 44px;
  }
  .brand-tagline {
    display: block;
    text-align: right;
    font-size: 22px;
    font-style: italic;
    margin-top: 4px;
  }
  .contacts {
    position: absolute;
    left: 24px;
    right: 24px;
    bottom: 26px;
    display: grid;
    grid-template-columns: 258px 228px 150px;
    column-gap: 2px;
    justify-content: space-between;
  }
  .contact {
    display: flex;
    flex-direction: column;
    align-items: center;
    text-align: center;
  }
  .contact-icon {
    height: 34px;
    display: flex;
    align-items: flex-end;
    padding-bottom: 4px;
  }
  .contact-value {
    display: block;
    width: 100%;
    height: 34px;
    line-height: 28px;
    border-top: 3px solid var(--ink-pale);
    white-space: nowrap;
    font-size: 12.5px;
    letter-spacing: -0.2px;
  }
  .contact--phone .contact-value {
    font-size: 19px;
    font-weight: 600;
    letter-spacing: 0.5px;
  }
</style>
</head>
<body>
<main class="sheet">

  <section class="card card--back" aria-label="Business card back">
    <div class="utensil-pattern" role="img" aria-label="Faint pattern of kitchen utensils, cups and pots"></div>
    <p class="back-message">Reach your health and weight loss goals with a plan designed just for you.</p>
    <div class="social">
      <span class="social-mark" aria-hidden="true"></span>
      <span class="social-handle">bramble_pantry</span>
    </div>
  </section>

  <section class="card card--front" aria-label="Business card front">
    <div class="utensil-pattern" role="img" aria-label="Faint pattern of kitchen utensils, cups and pots"></div>

    <div class="coach">
      <span class="coach-name">Rosalind Hartwell</span>
      <span class="coach-title">Health Coach</span>
    </div>

    <div class="brand">
      <h1 class="brand-name">Brambledown <span class="brand-sub">Pantry</span></h1>
      <span class="brand-tagline">where good health meets real life</span>
    </div>

    <div class="contacts">
      <div class="contact contact--email">
        <span class="contact-icon">
          <svg width="30" height="22" viewBox="0 0 30 22" aria-hidden="true">
            <rect x="2" y="3" width="26" height="17" fill="none" stroke="#cdeebe" stroke-width="2.5"/>
            <polyline points="2,3 15,13 28,3" fill="none" stroke="#cdeebe" stroke-width="2.5"/>
          </svg>
        </span>
        <span class="contact-value">rosalind@brambledownpantry-example.com</span>
      </div>
      <div class="contact contact--web">
        <span class="contact-icon">
          <svg width="28" height="28" viewBox="0 0 30 30" aria-hidden="true">
            <circle cx="15" cy="15" r="12" fill="none" stroke="#cdeebe" stroke-width="2.5"/>
            <ellipse cx="15" cy="15" rx="5" ry="12" fill="none" stroke="#cdeebe" stroke-width="2"/>
            <line x1="3" y1="15" x2="27" y2="15" stroke="#cdeebe" stroke-width="2"/>
          </svg>
        </span>
        <span class="contact-value">www.brambledownpantry-example.com</span>
      </div>
      <div class="contact contact--phone">
        <span class="contact-icon">
          <svg width="20" height="28" viewBox="0 0 20 30" aria-hidden="true">
            <rect x="2" y="2" width="16" height="26" rx="3" fill="none" stroke="#cdeebe" stroke-width="2.5"/>
            <circle cx="10" cy="23" r="1.6" fill="#cdeebe"/>
          </svg>
        </span>
        <span class="contact-value">(555) 274-8150</span>
      </div>
    </div>
  </section>

</main>
</body>
</html>
```